Vemtra Group: Business Card for a high end technology company

We need a cool new design for our business cards using our cloud logo. We are a technology consulting business. We pride ourselves on be the best of the best. We mainly focus on cloud solutions and managed services. We need a business card that sets us apart from the other technology companies in the area and allows us to stand out.

Target Market(s)

Technology departments, CIO, CEOs, and Information Technology Staff.

Industry/Entity Type

Information Technology

Contact Information for Business Card

Must have the logo and our name.
Must have employee name, email address, office phone, cell phone and website.
Need to have all info on one side a cool design on backside.

Font styles to use
Serif
Sans Serif

Requirements
Must have
• Must have the logo and our name.
• Must have employee name, email address, office phone, cell phone and website.
• Need to have all info on one side a cool design on back side.
• Must be a crisp clean design, not too busy or confusing.

```html
<!DOCTYPE html>
<html lang="en">
<head>
<meta charset="utf-8">
<title>Vemtra Group – Business Cards</title>
<link rel="stylesheet" href="https://fonts.googleapis.com/css2?family=Roboto:wght@400;700&display=swap">
<style>
  :root {
    --page-bg: #e9e6e1;
    --card-white: #ffffff;
    --card-grey: #d9d9d9;
    --blue-light: #3ea3ea;
    --blue-dark: #1769bd;
    --ink: #4a4a4a;
    --ink-dark: #2b2b2b;
    --white: #ffffff;
    --brand-dot: #2f8fdf;
  }
  * { box-sizing: border-box; margin: 0; padding: 0; }
  html, body {
    width: 1200px; height: 950px; overflow: hidden;
    background: var(--page-bg);
    font-family: "Roboto", Arial, sans-serif;
  }
  .sheet {
    width: 1200px; height: 950px;
    display: flex; flex-direction: column;
    align-items: center; justify-content: center; gap: 60px;
  }
  .card {
    width: 700px; height: 400px;
    box-shadow: 0 10px 28px rgba(0,0,0,.22);
    overflow: hidden;
  }
  /* Back side */
  .card-back {
    background: linear-gradient(135deg, var(--card-white) 0%, #f1f1f1 55%, var(--card-grey) 100%);
    display: flex; align-items: center; justify-content: center;
  }
  /* Front side */
  .card-front { display: flex; }
  .contact-panel {
    width: 50%; height: 100%;
    background: radial-gradient(circle at 70% 40%, var(--blue-light) 0%, var(--blue-dark) 85%);
    color: var(--white);
    padding: 46px 40px;
  }
  .person-name { font-size: 26px; font-weight: 700; line-height: 1.1; }
  .person-title { font-size: 19px; font-weight: 400; margin-top: 4px; }
  .contact-list { list-style: none; margin-top: 38px; }
  .contact-list li {
    display: flex; align-items: center; gap: 14px;
    font-size: 20px; line-height: 1; margin-bottom: 12px;
  }
  .contact-list svg { width: 18px; height: 18px; flex: none; }
  .brand-panel {
    width: 50%; height: 100%;
    background: linear-gradient(135deg, var(--card-white) 0%, #f3f3f3 60%, var(--card-grey) 100%);
    display: flex; align-items: center; justify-content: center;
  }
  .brand { display: flex; flex-direction: column; align-items: center; }
  .brand-line { display: flex; align-items: center; gap: 12px; }
  .brand-dot {
    width: 22px; height: 22px; border-radius: 50%;
    background: var(--brand-dot);
  }
  .brand-name {
    font-size: 44px; font-weight: 400; color: var(--ink);
    letter-spacing: .5px;
  }
  .brand-web {
    font-size: 13px; font-weight: 700; color: var(--ink-dark);
    margin-top: 8px;
  }
  .card-back .brand-name { font-size: 50px; }
</style>
</head>
<body>
<main class="sheet">
  <section class="card card-back" aria-label="Business card back">
    <div class="brand">
      <div class="brand-line">
        <span class="brand-dot"></span>
        <span class="brand-name">Vemtra Group</span>
      </div>
      <span class="brand-web">www.vemtragroup.com</span>
    </div>
  </section>

  <section class="card card-front" aria-label="Business card front">
    <div class="contact-panel">
      <h1 class="person-name">Marek Halden</h1>
      <p class="person-title">President</p>
      <ul class="contact-list">
        <li>
          <svg viewBox="0 0 24 24" fill="#fff" aria-hidden="true"><path d="M3 8c0-2 4-4 9-4s9 2 9 4v2h-5V8H8v2H3z"/><rect x="6" y="12" width="12" height="8" rx="1.5"/></svg>
          555 0142 7781
        </li>
        <li>
          <svg viewBox="0 0 24 24" fill="none" stroke="#fff" stroke-width="2.2" aria-hidden="true"><rect x="7" y="2" width="10" height="20" rx="2"/><line x1="11" y1="18" x2="13" y2="18"/></svg>
          555 0198 3364
        </li>
        <li>
          <svg viewBox="0 0 24 24" fill="#fff" aria-hidden="true"><path d="M2 6h20v12H2z"/><path d="M2 6l10 7 10-7" fill="none" stroke="#1e78c8" stroke-width="1.6"/></svg>
          marek@vemtra.net
        </li>
        <li>
          <svg viewBox="0 0 24 24" fill="none" stroke="#fff" stroke-width="2" aria-hidden="true"><circle cx="12" cy="12" r="9"/><ellipse cx="12" cy="12" rx="4" ry="9"/><line x1="3" y1="12" x2="21" y2="12"/></svg>
          www.vemtra.net
        </li>
      </ul>
    </div>
    <div class="brand-panel">
      <div class="brand">
        <div class="brand-line">
          <span class="brand-dot"></span>
          <span class="brand-name">Vemtra Group</span>
        </div>
        <span class="brand-web">www.vemtragroup.com</span>
      </div>
    </div>
  </section>
</main>
</body>
</html>
```